Update Law Firm Website

Update law firm website pages, add pages for employees. Current website looks stale. www.vantholmlegal.example

Target Market(s)

Personal injury clients

Industry/Entity Type

Legal

Number of Pages Required

5+ page

Font styles to use
Serif

Requirements
Must have
• User friendly and engaging design
Nice to have
• ?
Should not have
• scales of justice, law books,

```html
<!DOCTYPE html>
<html lang="en">
<head>
<meta charset="utf-8">
<title>Vantholm Legal</title>
<link href="https://fonts.googleapis.com/css2?family=Playfair+Display:wght@400&family=Noto+Serif:wght@400&family=Open+Sans:wght@400;600&display=swap" rel="stylesheet">
<style>
:root{
  --blue:#0b6fae;
  --blue-dark:#075a90;
  --red:#d4351f;
  --ink:#1c1c1c;
  --muted:#8a8a8a;
  --line:#e4e4e4;
  --hero:#ebebeb;
  --black:#0c0c0c;
  --band:#0b76b8;
}
*{margin:0;padding:0;box-sizing:border-box}
html,body{width:878px;height:1200px;overflow:hidden;background:#fff}
body{font-family:"Open Sans",Arial,sans-serif;color:var(--ink);font-size:7px}
.serif{font-family:"Noto Serif",Georgia,serif}
.wrap{width:532px;margin-left:173px;position:relative}
.btn{display:inline-block;background:linear-gradient(#1583c4,var(--blue-dark));color:#fff;font-family:"Noto Serif",Georgia,serif}
.dim{color:var(--muted);line-height:1.45;font-size:6px}

.topbar{height:12px;background:var(--black);color:#aaa;font-size:5.5px}
.topbar .wrap{display:flex;align-items:center;height:12px;gap:14px}
.topbar .social{margin-left:auto;display:flex;gap:5px}
.topbar .social i{width:4px;height:4px;border-radius:50%;background:#888;display:block}

.header{height:36px;border-bottom:1px solid var(--line)}
.header .wrap{display:flex;align-items:center;height:36px}
.brand{display:flex;align-items:center;gap:5px;font-family:"Playfair Display",Georgia,serif;font-size:15px}
.brand i{width:9px;height:9px;border-radius:50%;background:var(--blue);display:block}
.nav{margin-left:auto;display:flex;gap:0;font-size:6.5px;height:36px}
.nav a{width:52px;text-align:center;line-height:36px;color:var(--ink);text-decoration:none}
.nav a.active{color:var(--blue);border-bottom:1px solid var(--blue)}

.hero{height:210px;background:var(--hero);position:relative}
.hero .copy{position:absolute;left:173px;top:50px}
.hero h1{font-family:"Playfair Display",Georgia,serif;font-weight:400;font-size:36px;line-height:1}
.hero h2{font-family:"Noto Serif",Georgia,serif;font-weight:400;font-size:13px;margin:8px 0 10px}
.hero p{width:200px;color:#555;font-size:6px;line-height:1.5}
.hero .btn{margin-top:12px;font-size:6px;padding:5px 11px}
.hero .photo{position:absolute;left:440px;top:10px;width:220px;height:200px;background:linear-gradient(160deg,#d6d6d6,#5a5a5a 70%,#2b2b2b)}

.features{display:flex;justify-content:space-between;padding-top:18px;height:100px}
.feature{width:122px}
.feature h3{display:flex;align-items:center;gap:8px;font-family:"Noto Serif",Georgia,serif;font-weight:400;font-size:8px;color:#444}
.feature h3 i{width:15px;height:15px;border-radius:50%;background:var(--blue);display:block}
.feature p{margin:10px 0 12px}
.more{color:var(--blue);font-family:"Noto Serif",Georgia,serif;font-size:6px}

.callout{display:flex;border:1px solid var(--line);height:46px}
.callout .text{flex:1;padding:11px 18px}
.callout h4{font-family:"Noto Serif",Georgia,serif;font-weight:400;font-size:8px;margin-bottom:4px}
.callout .action{width:134px;border-left:1px solid var(--line);display:flex;align-items:center;justify-content:center}
.callout .btn{font-size:7.5px;padding:6px 15px}

.section-title{display:flex;align-items:center;justify-content:space-between;font-family:"Noto Serif",Georgia,serif;font-size:8.5px;margin-bottom:10px}
.arrows{display:flex;gap:1px}
.arrows i{width:8px;height:7px;background:var(--black);display:block}
.rule{border-top:1px solid #efefef}

.practice{padding:16px 0 16px;margin-top:16px}
.gallery{display:flex;justify-content:space-between}
.gallery div{width:126px;height:80px;background:linear-gradient(135deg,#dcdcdc,#7c7c7c)}

.split{display:flex;justify-content:space-between;padding:14px 0 12px;height:166px}
.news,.testi{width:260px}
.post{display:flex;gap:9px;margin-bottom:10px}
.date{width:21px;text-align:center;flex:none}
.date b{display:block;background:var(--blue);color:#fff;font-family:"Noto Serif",Georgia,serif;font-weight:400;font-size:8px;line-height:17px}
.date span{display:block;background:var(--black);color:#fff;font-size:4.5px;line-height:8px}
.post h5{font-family:"Noto Serif",Georgia,serif;font-weight:400;font-size:6.5px}
.post .by{font-size:5px;color:var(--muted);margin:2px 0 4px}
.post .by em{font-style:normal;color:var(--red)}
.quote{border:1px solid var(--line);padding:12px 14px 14px 34px;position:relative;font-family:"Noto Serif",Georgia,serif;font-size:6.3px;line-height:1.7;color:#555}
.quote:before{content:"\201C";position:absolute;left:12px;top:4px;color:var(--red);font-size:16px}
.author{display:flex;align-items:center;gap:7px;margin-top:10px;font-size:5.5px}
.author .avatar{width:18px;height:18px;background:#9a9a9a}
.author b{display:block;color:var(--red);font-family:"Noto Serif",Georgia,serif;font-weight:400;font-size:6px}

.team{padding-top:14px;height:240px}
.members{display:flex;justify-content:space-between}
.member{width:126px;border:1px solid var(--line);height:180px;text-align:center}
.member .portrait{height:88px;background:linear-gradient(#e6e6e6,#8d8d8d)}
.member .name{width:100px;margin:-12px auto 0;background:#fff;border:1px solid var(--line);position:relative;padding:3px 0}
.member .name b{display:block;font-family:"Noto Serif",Georgia,serif;font-weight:400;font-size:6.5px}
.member .name span{color:var(--red);font-size:5px}
.member p{margin:9px 12px 8px}
.member .btn{font-size:6px;padding:4px 12px}

.clients{padding-top:14px;height:88px}
.logos{display:flex;justify-content:space-between;align-items:center;padding:6px 0 0}
.logos span{display:flex;align-items:center;gap:4px;font-family:"Noto Serif",Georgia,serif;font-size:11px;color:#8a8a8a}
.logos span i{width:7px;height:7px;border-radius:50%;background:#8a8a8a;display:block}

.band{height:22px;background:var(--band);color:#fff;font-size:5.5px}
.band .wrap{display:flex;align-items:center;height:22px;gap:10px}
.band .dot{width:6px;height:6px;border-radius:50%;background:#fff}
.band .pager{margin-left:auto;display:flex;gap:1px}
.band .pager i{width:8px;height:7px;background:#fff;display:block;opacity:.85}

.footer{background:var(--black);color:#9a9a9a;height:256px;padding-top:20px;font-size:5.5px}
.footer .cols{display:flex;justify-content:space-between}
.footer .col{width:126px}
.footer .brand{color:#fff;font-size:11px;margin-bottom:22px}
.footer h6{color:#fff;font-family:"Noto Serif",Georgia,serif;font-weight:400;font-size:7px;border-bottom:1px solid #2a2a2a;padding:5px 0 8px;margin-bottom:14px}
.footer li{list-style:none;border-bottom:1px solid #222;padding:3px 0 4px 8px;color:#ccc}
.contact-row{display:flex;gap:9px;margin-top:11px;line-height:1.5;color:#bbb}
.contact-row svg{flex:none}
.field{height:13px;border:1px solid #333;background:#111;margin:4px 0 10px}
.field.area{height:38px}
.submit{display:inline-block;background:#fff;color:#222;padding:3px 10px;font-size:5.5px}
.copyright{border-top:1px solid #222;margin-top:24px;padding-top:8px;color:#666;font-size:5px}
</style>
</head>
<body>

<div class="topbar">
  <div class="wrap">
    <span>Call us: 1-800-555-0142</span>
    <span>contact@vantholmlegal.example</span>
    <div class="social"><i></i><i></i><i></i><i></i><i></i></div>
  </div>
</div>

<header class="header">
  <div class="wrap">
    <div class="brand"><i></i>Vantholm Legal</div>
    <nav class="nav">
      <a class="active" href="#">Home</a><a href="#">About us</a><a href="#">Services</a><a href="#">Blogs</a><a href="#">Contacts</a>
    </nav>
  </div>
</header>

<section class="hero">
  <div class="copy">
    <h1>Qualified</h1>
    <h2>legal advice.</h2>
    <p>Lorem ipsum dolor sit amet, consectetur ipiscing elit. Phasellus pellentesque posuere risus lacinia tristique usce sed massa sodales facilisis.</p>
    <span class="btn">Read More</span>
  </div>
  <div class="photo" role="img" aria-label="Black and white portrait of a smiling attorney in glasses and a suit"></div>
</section>

<div class="wrap">
  <section class="features">
    <div class="feature"><h3><i></i>Solid Law Practic</h3><p class="dim">Lorem ipsum dolor sit amet, consectetur adipiscing elit. Phasellus pellentesque posuere risus lacinia tristique.</p><span class="more">Read More ›</span></div>
    <div class="feature"><h3><i></i>General Practice</h3><p class="dim">Lorem ipsum dolor sit amet, consectetur adipiscing elit. Phasellus pellenesque posere risus lacinia tristique.</p><span class="more">Read More ›</span></div>
    <div class="feature"><h3><i></i>Business Solution</h3><p class="dim">Lorem ipsum dolor sit amet, consectetur adipiscing elit. Phasellus llentesque posuere risus lacinia tristiqu</p><span class="more">Read More ›</span></div>
    <div class="feature"><h3><i></i>Wide Experience</h3><p class="dim">Lorem ipsum dolor sit amet, consectetur adipiscing elit. Phasellus pelltesque posuere risus lacinia tristique.</p><span class="more">Read More ›</span></div>
  </section>

  <section class="callout">
    <div class="text">
      <h4>All people are equal before the law. A good attorney is what makes a difference.</h4>
      <p class="dim">Lorem ipsum dolor sit met, conteturing elit. Phasellus pellentesque osure risus lacinia tristique Fusce sed massa</p>
    </div>
    <div class="action"><span class="btn">Download</span></div>
  </section>

  <section class="practice rule">
    <div class="section-title">Solid Law Practic<div class="arrows"><i></i><i></i></div></div>
    <div class="gallery">
      <div role="img" aria-label="Hand holding a signed contract"></div>
      <div role="img" aria-label="Businessman celebrating at his desk"></div>
      <div role="img" aria-label="Documents being reviewed across a table"></div>
      <div role="img" aria-label="Two colleagues in a meeting"></div>
    </div>
  </section>

  <section class="split rule">
    <div class="news">
      <div class="section-title">Latest News</div>
      <article class="post">
        <div class="date"><b>21</b><span>DEC</span></div>
        <div><h5>How We Can Help You</h5><p class="by">by <em>Tom Harlow</em> Comments <em>(4)</em></p><p class="dim">Lorem ipsum dolor sit amet, consectetur ipiscing elit. Phasellus pelntesque posure risus lacinia tristique. Fusce sed massa id mi soles facilisis. Quisque augue eleifend non consequat scelerisque dapibus in enim.</p></div>
      </article>
      <article class="post">
        <div class="date"><b>23</b><span>DEC</span></div>
        <div><h5>New Team Members</h5><p class="by">by <em>Tom Harlow</em> Comments <em>(4)</em></p><p class="dim">Lorem ipsum dolor sit amet, contetur adipiscing elit. Phasellus pellentesque posure risus lacinia tristique. Fusce sed massa id mi les facilisis. Quisque augue eleifend consequat scelerisque dapibus in enim.</p></div>
      </article>
    </div>
    <div class="testi">
      <div class="section-title">Testimonials<div class="arrows"><i></i><i></i></div></div>
      <div class="quote">Lorem ipsum dolor sit amet, consectetur adipiscing elit. Phasellus pellentesque posure risus lacinia tristique. Fusce sed massa id mi sodales facilisis. Quisque augue eleifend non consequat scelerisque dapibus in enim. Sed tempus turpis at tellus</div>
      <div class="author"><div class="avatar" role="img" aria-label="Client portrait"></div><div><b>Owen Radley</b>Radley Freight</div></div>
    </div>
  </section>

  <section class="team rule">
    <div class="section-title">Our Team</div>
    <div class="members">
      <div class="member"><div class="portrait" role="img" aria-label="Portrait of senior attorney"></div><div class="name"><b>Hugh Carrow</b><span>Attorney</span></div><p class="dim">Lorem ipsum dolor sit met, conteturing elit. Phasellus pellentesque osure risus lacinia</p><span class="btn">Profile</span></div>
      <div class="member"><div class="portrait" role="img" aria-label="Portrait of attorney"></div><div class="name"><b>Peter Ansel</b><span>Attorney</span></div><p class="dim">Lorem ipsum dolor sit met, conteturing elit. Phasellus pellentesque osure risus lacinia</p><span class="btn">Profile</span></div>
      <div class="member"><div class="portrait" role="img" aria-label="Portrait of attorney"></div><div class="name"><b>Clara Wendt</b><span>Attorney</span></div><p class="dim">Lorem ipsum dolor sit met, conteturing elit. Phasellus pellentesque osure risus lacinia</p><span class="btn">Profile</span></div>
      <div class="member"><div class="portrait" role="img" aria-label="Portrait of attorney"></div><div class="name"><b>Nora Baines</b><span>Attorney</span></div><p class="dim">Lorem ipsum dolor sit met, conteturing elit. Phasellus pellentesque osure risus lacinia</p><span class="btn">Profile</span></div>
    </div>
  </section>

  <section class="clients rule">
    <div class="section-title">Clients</div>
    <div class="logos">
      <span><i></i>Brantwood</span><span>Lunette</span><span><i></i>Greystone</span><span><i></i>Ironvale</span><span>Marlowe</span>
    </div>
  </section>
</div>

<div class="band">
  <div class="wrap">
    <span class="dot"></span>
    <span>Lorem ipsum dolor sit amet, consectetur adipiscing elit. Phasellus id enim felis. uis sed bibendum eros. Cras at risus id tellus vehicula volutpat</span>
    <div class="pager"><i></i><i></i></div>
  </div>
</div>

<footer class="footer">
  <div class="wrap">
    <div class="cols">
      <div class="col">
        <div class="brand"><i></i>Law Business</div>
        <p>Lorem Ipsum is simply dummy text of the rinting and typesetting industry. Lorem</p>
        <div class="contact-row"><svg width="6" height="8" viewBox="0 0 6 8"><path d="M3 0a3 3 0 0 1 3 3c0 2-3 5-3 5S0 5 0 3a3 3 0 0 1 3-3z" fill="#fff"/></svg><span>Vantholm Legal Ltd.<br>Street Name 123<br>123 45 Cityname</span></div>
        <div class="contact-row"><svg width="6" height="8" viewBox="0 0 6 8"><rect x="1" y="0" width="4" height="8" rx="1" fill="#fff"/></svg><span>+123 900 123 456</span></div>
        <div class="contact-row"><svg width="7" height="6" viewBox="0 0 7 6"><rect width="7" height="6" fill="#fff"/><path d="M0 0l3.5 3L7 0" stroke="#000" fill="none" stroke-width=".8"/></svg><span>info@vantholmlegal.example</span></div>
      </div>
      <div class="col">
        <h6>Services</h6>
        <ul><li>How to Write a Blog</li><li>Create a Blog in 4 Steps</li><li>15 Tips to Increase Traffic</li><li>20 Blog Post Ideas</li><li>How to Write a Blog</li><li>Create a Blog in 4 Steps</li><li>15 Tips to Increase Traffic</li></ul>
      </div>
      <div class="col">
        <h6>Attorney</h6>
        <ul><li>How to Write a Blog</li><li>Create a Blog in 4 Steps</li><li>15 Tips to Increase Traffic</li><li>20 Blog Post Ideas</li><li>How to Write a Blog</li><li>Create a Blog in 4 Steps</li><li>15 Tips to Increase Traffic</li></ul>
      </div>
      <div class="col">
        <h6>Contact Form</h6>
        <p>Enter Email address</p><div class="field"></div>
        <p>Enter your question</p><div class="field area"></div>
        <span class="submit">Submit</span>
      </div>
    </div>
    <div class="copyright">© 2015 Vantholm Legal. Powered by Fieldwork Studio</div>
  </div>
</footer>

</body>
</html>
```